Business card design

I need my logo on this card, things I need the card to have on it
licensed and insured.
owner operators Milo & Dalton Whitby
my phone number 5550138274
Disaster Recovery, Storm Damage Restoration, Proactive Disaster Plan Management, Roof Repair/Restoration Structural Repair and Reconstruction, Emergency Boarding and Tarping Service, Perimeter Fencing, Emergency Tree Removal,

```html
<!DOCTYPE html>
<html lang="en">
<head>
<meta charset="utf-8">
<title>Whitby's Construction – Business Card</title>
<link rel="stylesheet" href="https://fonts.googleapis.com/css2?family=Nunito:wght@400;600&family=Raleway:wght@400;500&display=swap">
<style>
  :root {
    --bg: #9b9b9b;
    --brand-blue: #3d95d3;
    --brand-blue-deep: #2f7fc0;
    --brand-gray: #6d6e71;
    --ink: #1f1f1f;
    --white: #ffffff;
  }
  * { box-sizing: border-box; margin: 0; padding: 0; }
  html, body { width: 1093px; height: 1200px; overflow: hidden; }
  body {
    background: var(--bg);
    font-family: "Nunito", sans-serif;
    position: relative;
  }
  .card {
    position: absolute;
    border-radius: 18px;
    overflow: hidden;
  }
  /* Front: services side */
  .card--front {
    left: 265px; top: 224px; width: 580px; height: 362px;
    background: var(--brand-blue);
    color: var(--white);
    text-align: center;
  }
  .front-brand {
    position: absolute; left: 0; right: 0; top: 156px;
    display: flex; justify-content: center; align-items: center; gap: 10px;
    font-family: "Nunito", sans-serif; font-weight: 400;
    font-size: 22px; letter-spacing: 1px;
    color: var(--brand-blue-deep);
    white-space: nowrap;
  }
  .front-brand .mark {
    width: 12px; height: 12px; background: var(--brand-blue-deep); flex: none;
  }
  .services-title {
    position: absolute; left: 0; right: 0; top: 222px;
    font-family: "Raleway", sans-serif; font-weight: 500; font-size: 19px;
  }
  .services-rule {
    position: absolute; left: 220px; width: 136px; top: 249px;
    height: 1px; background: rgba(255,255,255,0.85);
  }
  .services-list {
    position: absolute; left: 0; right: 0; top: 268px;
    list-style: none; font-size: 14px; line-height: 25px;
  }
  .services-list li span::before {
    content: "●"; font-size: 9px; margin: 0 4px 0 6px; vertical-align: 2px;
  }
  /* Back: contact side */
  .card--back {
    left: 261px; top: 619px; width: 596px; height: 363px;
    background: var(--white);
  }
  .back-brand {
    position: absolute; left: 38px; width: 230px; top: 160px;
    display: flex; align-items: center; justify-content: center; gap: 7px;
    font-weight: 400; font-size: 15px; letter-spacing: 0.5px; color: var(--brand-blue);
    white-space: nowrap;
  }
  .back-brand .mark { width: 10px; height: 10px; background: var(--brand-blue); flex: none; }
  .divider {
    position: absolute; left: 293px; top: 83px; width: 1px; height: 176px;
    background: var(--brand-gray);
  }
  .contact { position: absolute; left: 304px; top: 83px; color: var(--ink); }
  .owners { font-size: 22px; color: var(--brand-blue); font-weight: 400; line-height: 28px; white-space: nowrap; }
  .role { font-size: 13px; margin-top: 1px; }
  .address { font-size: 13.5px; line-height: 16px; margin-top: 16px; font-style: normal; }
  .contact-lines { list-style: none; margin-top: 12px; font-size: 13.5px; }
  .contact-lines li { display: flex; align-items: center; gap: 9px; height: 24px; }
  .contact-lines svg { width: 15px; height: 15px; flex: none; }
  .band-line {
    position: absolute; left: 0; right: 0; top: 321px; height: 4px; background: var(--brand-gray);
  }
  .band {
    position: absolute; left: 0; right: 0; top: 327px; bottom: 0; background: var(--brand-blue);
    display: flex; align-items: center; justify-content: center;
  }
  .credentials {
    color: var(--white); font-size: 12px; font-weight: 600; letter-spacing: 2px; text-transform: uppercase;
  }
</style>
</head>
<body>
  <section class="card card--front">
    <div class="front-brand"><span class="mark"></span>WHITBY'S CONSTRUCTION L.L.C</div>
    <h2 class="services-title">OUR SERVICES</h2>
    <div class="services-rule"></div>
    <ul class="services-list">
      <li><span>Disaster Recovery</span><span>Storm Damage Restoration</span><span>Proactive Disaster Plan Management</span></li>
      <li><span>Roof Repair/Restoration Structural Repair and Reconstruction</span><span>Perimeter Fencing</span></li>
      <li><span>Emergency Boarding and Tarping Service</span><span>Emergency Tree Removal</span></li>
    </ul>
  </section>

  <section class="card card--back">
    <div class="back-brand"><span class="mark"></span>WHITBY'S CONSTRUCTION</div>
    <div class="divider"></div>
    <div class="contact">
      <h1 class="owners">Milo &amp; Dalton Whitby</h1>
      <p class="role">owner operators</p>
      <address class="address">48 Cedar Hollow Lane<br>Brandon, MS 39042</address>
      <ul class="contact-lines">
        <li>
          <svg viewBox="0 0 16 16" aria-hidden="true"><path fill="#3d95d3" d="M1 6c0-2 3-3 7-3s7 1 7 3v1h-3V5.5H4V7H1z"/><path fill="#3d95d3" d="M4 8h8l1 6H3z"/><circle cx="8" cy="11" r="1.6" fill="#fff"/></svg>
          <span>5550138274</span>
        </li>
        <li>
          <svg viewBox="0 0 16 16" aria-hidden="true"><rect x="1" y="3" width="14" height="10" rx="1" fill="#3d95d3"/><path d="M1.5 4l6.5 5 6.5-5" fill="none" stroke="#fff" stroke-width="1.2"/></svg>
          <span>info@whitbybuild.com</span>
        </li>
        <li>
          <svg viewBox="0 0 16 16" aria-hidden="true"><circle cx="8" cy="8" r="7" fill="#3d95d3"/><path d="M1 8h14M8 1c-3 3-3 11 0 14M8 1c3 3 3 11 0 14" fill="none" stroke="#fff" stroke-width="1"/></svg>
          <span>www.whitbybuild.com</span>
        </li>
      </ul>
    </div>
    <div class="band-line"></div>
    <div class="band"><p class="credentials">Licensed and Insured</p></div>
  </section>
</body>
</html>
```